Meadowlark Bloom Yard Website

I am looking for a website that allows me to be able to work on and make changes. I am looking to upload pictures to showcase my flowers, activities, and venue option at my garden. I am NOT tech savvy at all. I am looking to build my brand, and have options for click and purchase flowers or activities and or pay with swipe. I want to add my instagram and facebook pages and link those pages to each other. Also I would like to have a way to get their info for email updates on my new business. I want to advertise that my site is new and we are working at planting our Spring Flowers ;)

I want to be able to work on my website myself with ease. I want my products page to be easy to access - user friendly.

Target Market(s)

Local Florist, Grocers, growers, event venues, local flower farmers

Industry/Entity Type

Hospitality

Coding

Coded - Design and coding required

Number of Pages Required

5+ page

Font styles to use
Decorative

Requirements
Must have
• Must have radio buttons for my clients to sign up for contact page, be able to call and email me, find my facebook and instagram icon, select events, classes, merchandise and flower arrangements and pay with apple pay, venmo and square
Nice to have
• I am very much looking for something very similar to this website. Please refer to https://www.brindlewoodstems.com for what I desir. I have uploaded photographs, and my logo. I will also like on my homepage where all my flowers are to be able to write a brief introduction/brand
Should not have
• Any hidden secrets on how to add photos, change out photos or be difficult to manage

```html
<!DOCTYPE html>
<html lang="en">
<head>
<meta charset="utf-8">
<title>Meadowlark Bloom Yard</title>
<link href="https://fonts.googleapis.com/css2?family=Playfair+Display:wght@400;700&family=Lato:wght@400;700&display=swap" rel="stylesheet">
<style>
:root{
  --backdrop:#f4ecdc;
  --page:#ffffff;
  --ink:#222222;
  --muted:#8a8a8a;
  --line:#e6e6e6;
  --panel:#f3f3f3;
  --accent:#d13a4c;
  --tile:#eeeeee;
}
*{box-sizing:border-box;margin:0;padding:0}
html,body{width:1200px;height:2280px;overflow:hidden}
body{background:var(--backdrop);font-family:'Lato',sans-serif;color:var(--ink);position:relative}
.page{position:absolute;left:180px;top:0;width:840px;height:2280px;background:var(--page)}
.abs{position:absolute}
.brand{left:0;width:840px;top:38px;text-align:center;font-family:'Playfair Display',serif;font-weight:700;font-size:22px;letter-spacing:1px;color:var(--ink)}
.nav{top:88px;left:12px;right:12px;height:18px;display:flex;align-items:center;font-size:8px;letter-spacing:1px;color:var(--ink)}
.nav .search{display:flex;align-items:center;gap:6px;width:200px}
.nav ul{list-style:none;display:flex;gap:34px;flex:1;justify-content:center}
.nav li.active{color:var(--accent)}
.nav .cart{width:200px;text-align:right;display:flex;justify-content:flex-end;align-items:center;gap:6px}
.photo{background:linear-gradient(135deg,#e9e2d6,#d9cfc0)}
.hero{left:12px;top:136px;width:816px;height:396px;background:linear-gradient(120deg,#c7b9a6 0%,#ede3d3 35%,#efe6d8 65%,#b9a994 100%)}
.hero-text{left:420px;top:300px;width:300px;text-align:center;font-family:'Playfair Display',serif;font-size:24px;line-height:1.3;color:var(--ink)}
.hero-link{left:420px;top:388px;width:300px;text-align:center;font-size:9px;text-decoration:underline;letter-spacing:.5px}
.cats{top:568px;left:12px;width:816px;display:flex;justify-content:space-between}
.cat{width:112px;text-align:center}
.cat .img{width:112px;height:120px;background:linear-gradient(160deg,#f5f5f5,#e2e2e2)}
.cat p{margin-top:22px;font-size:7px;letter-spacing:1px}
.quote-box{left:12px;top:760px;width:816px;height:288px;background:var(--panel)}
.quote-corner-l{left:12px;top:908px;width:70px;height:130px;background:linear-gradient(180deg,#e8b4b0,#c86d68)}
.quote-corner-r{left:758px;top:762px;width:68px;height:110px;background:linear-gradient(180deg,#d96a66,#e9c7c3)}
.avatar{left:404px;top:826px;width:32px;height:32px;border-radius:50%;background:linear-gradient(135deg,#f2c060,#d14a3f)}
.quote{left:220px;top:896px;width:400px;text-align:center;font-family:'Playfair Display',serif;font-size:14px;line-height:1.5;color:#444}
.quote-name{left:0;width:840px;top:962px;text-align:center;font-size:7px;letter-spacing:1px;color:var(--muted)}
.arrow{top:888px;width:40px;height:1px;background:#aaa}
.section-label{left:12px;top:1084px;font-size:7px;letter-spacing:1px}
.pager{right:12px;top:1082px;display:flex;gap:8px}
.products{top:1112px;left:12px;width:816px;display:flex;justify-content:space-between}
.product{width:192px;position:relative;text-align:center}
.product .img{width:192px;height:248px;background:linear-gradient(170deg,#fafafa,#e6e6e6)}
.badge{position:absolute;top:6px;left:6px;background:var(--ink);color:#fff;font-size:6px;padding:3px 6px;letter-spacing:1px}
.badge.sale{left:auto;right:6px;background:var(--accent)}
.product h3{margin-top:18px;font-size:7px;font-weight:400;letter-spacing:1px}
.product span{display:block;margin-top:8px;font-size:7px;color:var(--muted)}
.about-title{left:12px;top:1470px;font-family:'Playfair Display',serif;font-size:24px;line-height:1.3}
.about-title em{font-style:normal;color:var(--accent)}
.about-text{left:12px;top:1556px;width:380px;font-size:9px;line-height:1.7;color:#666}
.about-img{left:420px;top:1464px;width:408px;height:264px;background:linear-gradient(135deg,#e9e4dd,#6d7a5c 70%,#3a3a3a)}
.news{left:12px;top:1780px;width:816px;height:260px;background:var(--panel)}
.news h2{position:absolute;left:0;right:0;top:80px;text-align:center;font-family:'Playfair Display',serif;font-size:17px;font-weight:400}
.news .field{position:absolute;left:218px;top:128px;width:270px;height:34px;background:#fff;font-size:8px;color:var(--muted);padding:12px}
.news .btn{position:absolute;left:496px;top:128px;width:106px;height:34px;background:var(--ink);color:#fff;font-size:8px;letter-spacing:1px;text-align:center;line-height:34px}
.footer{top:2068px;left:12px;width:816px;display:flex;justify-content:space-between}
.col{width:170px}
.col h4{font-size:7px;letter-spacing:1px;font-weight:700;margin-bottom:10px}
.col li{list-style:none;font-size:7px;color:var(--muted);line-height:2}
.bottom{top:2248px;left:12px;width:816px;display:flex;justify-content:space-between;align-items:center;font-size:6px;color:var(--muted)}
.pay{display:flex;gap:4px}
.pay i{display:block;width:18px;height:11px;background:#ddd}
.pay i.dark{background:#555}
</style>
</head>
<body>
<div class="page">
  <div class="abs brand">MEADOWLARK BLOOM YARD</div>

  <nav class="abs nav">
    <div class="search">
      <svg width="10" height="10" viewBox="0 0 10 10"><circle cx="4" cy="4" r="3" fill="none" stroke="#222"/><line x1="6.2" y1="6.2" x2="9.5" y2="9.5" stroke="#222"/></svg>
      SEARCH
    </div>
    <ul>
      <li class="active">HOME</li><li>SHOP</li><li>EVENTS</li><li>PORTFOLIO</li><li>BLOG</li><li>CLASSES</li>
    </ul>
    <div class="cart">
      <svg width="10" height="10" viewBox="0 0 10 10"><rect x="1.5" y="3" width="7" height="6" fill="none" stroke="#222"/><path d="M3.5 3V2a1.5 1.5 0 0 1 3 0v1" fill="none" stroke="#222"/></svg>
      CART (0)
    </div>
  </nav>

  <div class="abs hero" role="img" aria-label="Flat lay of fresh tulips, roses, scissors and twine around kraft paper on a white wooden table"></div>
  <div class="abs hero-text">Let's make beautiful<br>flowers a part of your life.</div>
  <div class="abs hero-link">Start Shopping</div>

  <div class="abs cats">
    <div class="cat"><div class="img" role="img" aria-label="Orange flowers in a glass vase"></div><p>CUT FLOWERS</p></div>
    <div class="cat"><div class="img" role="img" aria-label="Pink tulip"></div><p>GARDEN</p></div>
    <div class="cat"><div class="img" role="img" aria-label="Green houseplant"></div><p>BRIDAL</p></div>
    <div class="cat"><div class="img" role="img" aria-label="Red lily"></div><p>POTTED</p></div>
    <div class="cat"><div class="img" role="img" aria-label="Pink lily stem"></div><p>EVENTS</p></div>
    <div class="cat"><div class="img" role="img" aria-label="Succulent plant"></div><p>CLASSES</p></div>
  </div>

  <div class="abs quote-box"></div>
  <div class="abs quote-corner-l photo" role="img" aria-label="Red flower stem in the corner"></div>
  <div class="abs quote-corner-r photo" role="img" aria-label="Red blossoms hanging from the corner"></div>
  <div class="abs avatar" role="img" aria-label="Small round flower emblem"></div>
  <div class="abs arrow" style="left:240px"></div>
  <div class="abs arrow" style="left:560px"></div>
  <div class="abs quote">Fresh stems every week, arranged with care and delivered with a smile to your door.</div>
  <div class="abs quote-name">HANNAH ROWE</div>

  <div class="abs section-label">FEATURED ITEMS</div>
  <div class="abs pager">
    <svg width="8" height="8" viewBox="0 0 8 8"><path d="M5 1L2 4l3 3" fill="none" stroke="#222"/></svg>
    <svg width="8" height="8" viewBox="0 0 8 8"><path d="M3 1l3 3-3 3" fill="none" stroke="#222"/></svg>
  </div>

  <div class="abs products">
    <div class="product"><div class="img" role="img" aria-label="Round cactus in a white pot"></div><span class="badge">NEW</span><h3>CACTUS IN WHITE POT</h3><span>$24.00</span></div>
    <div class="product"><div class="img" role="img" aria-label="Red lily bloom"></div><h3>RED LILY STEM</h3><span>$18.00</span></div>
    <div class="product"><div class="img" role="img" aria-label="Two pink tulips"></div><h3>PINK TULIP PAIR</h3><span>$12.00</span></div>
    <div class="product"><div class="img" role="img" aria-label="Flowering cactus in a brass pot"></div><span class="badge sale">SALE</span><h3>BRASS POT CACTUS</h3><span>$32.00</span></div>
  </div>

  <div class="abs about-title">We take <em>flowers</em> personally<br>&amp; we bring you happiness</div>
  <div class="abs about-text">Our garden is brand new and we are busy planting spring flowers for the season ahead. Visit the yard, join a class, book the venue for your event, or order a bouquet grown right here. Stems are picked at dawn and arranged by hand for local shops, growers and friends.<br><br>Sign up below to hear when new blooms are ready.</div>
  <div class="abs about-img" role="img" aria-label="Person holding a woven basket of potted succulents beside a shelf"></div>

  <div class="abs news">
    <h2>Join The Colorful Bunch!</h2>
    <div class="field">Your email address</div>
    <div class="btn">SUBSCRIBE</div>
  </div>

  <div class="abs footer">
    <div class="col"><h4>CUSTOMER SERVICE</h4><ul><li>Help &amp; Contact</li><li>Returns &amp; Refunds</li><li>Online Stores</li><li>Terms of Use</li></ul></div>
    <div class="col"><h4>COMPANY</h4><ul><li>About Us</li><li>Our Story</li><li>Garden Visits</li><li>Venue Hire</li><li>Classes</li></ul></div>
    <div class="col"><h4>SOCIAL MEDIA</h4><ul><li>Photo Feed</li><li>Community</li><li>Newsletter</li><li>Journal</li></ul></div>
    <div class="col"><h4>SHIPPING</h4><ul><li>Delivery Areas</li><li>Local Pickup</li><li>Order Status</li><li>Gift Cards</li><li>Wholesale</li></ul></div>
  </div>

  <div class="abs bottom">
    <span>© 2024 Meadowlark Bloom Yard</span>
    <div class="pay"><i></i><i class="dark"></i><i></i><i></i></div>
    <span>Privacy Policy</span>
  </div>
</div>
</body>
</html>
```